Optometrist/Eye Care Clinic Business card with new logo attached

We are a small, independent eye care clinic in Canada. We have recently updated our logo (as attached), and would like a professional, modern and health care oriented business card to highlight our office details and our optometrist. We'd like to incorporate the blue colours as seen on our logo.

Target Market(s)

demographic: age 35-65 male/female equal

Industry/Entity Type

Health Care

Contact Information for Business Card

Name of clinic: "Amber Hollow Eye Care Optometry"

Font styles to use
Sans Serif

Colors
0355a3

Requirements
Must have
• our website: amberholloweyecare.net
• Dr Selma Okonkwo
• Optometrist
• 312-617 E Larkspur Ave
• Vancouver BC V7R 3P8
• P: 604-555-0193
• E: info@amberholloweyecare.net
Nice to have
• front side: logo/name of clinic as seen on logo attached and website
• backside: logo on the left side, and name/title/address/phone/email

```html
<!DOCTYPE html>
<html lang="en">
<head>
<meta charset="utf-8">
<title>Amber Hollow Eye Care Optometry – Business Card</title>
<link rel="stylesheet" href="https://fonts.googleapis.com/css2?family=Nunito+Sans:wght@400;600&display=swap">
<style>
  :root {
    --brand-blue: #0355a3;
    --sky-blue: #1aa3dc;
    --pale-blue: #a9d8ee;
    --ink: #2a1f1a;
    --text: #222;
    --paper: #ffffff;
    --backdrop: #e6e8eb;
  }
  * { box-sizing: border-box; margin: 0; padding: 0; }
  html, body { width: 1200px; height: 900px; overflow: hidden; }
  body {
    background: var(--backdrop);
    font-family: "Nunito Sans", sans-serif;
    display: flex; flex-direction: column; align-items: center; justify-content: center;
    gap: 60px;
  }
  .card {
    position: relative; width: 620px; height: 354px;
    background: var(--paper); border-radius: 22px; overflow: hidden;
    box-shadow: 0 6px 18px rgba(0,0,0,.15);
  }
  .clinic-name {
    color: var(--brand-blue); font-weight: 400; text-transform: uppercase;
    text-align: center; line-height: 1.15; letter-spacing: .12em;
  }
  .clinic-name .line-lg { display: block; font-size: 30px; }
  .clinic-name .line-md { display: block; font-size: 22px; }
  .clinic-name .line-sm { display: block; font-size: 13px; letter-spacing: .5em; margin-top: 4px; }
  .mark-dot {
    width: 64px; height: 64px; border-radius: 50%;
    background: var(--brand-blue); margin: 0 auto 14px;
  }

  /* Front */
  .card-front .brand { position: absolute; top: 62px; left: 0; right: 0; }
  .card-front .web-band {
    position: absolute; left: 0; right: 0; bottom: 0; height: 48px;
    background: var(--brand-blue); color: #fff;
    display: flex; align-items: center; justify-content: center;
    font-size: 19px; letter-spacing: .02em;
  }

  /* Back */
  .card-back .waves { position: absolute; inset: 0; }
  .card-back .brand { position: absolute; top: 88px; left: 40px; width: 220px; }
  .card-back .brand .line-lg { font-size: 21px; }
  .card-back .brand .line-md { font-size: 16px; }
  .card-back .brand .line-sm { font-size: 10px; }
  .card-back .brand .mark-dot { width: 48px; height: 48px; margin-bottom: 10px; }
  .divider {
    position: absolute; left: 290px; top: 50px; width: 2px; height: 190px;
    background: linear-gradient(to bottom, transparent, #c9ccd2 30%, #c9ccd2 70%, transparent);
  }
  .contact { position: absolute; left: 320px; top: 58px; }
  .doctor-name { font-size: 25px; font-weight: 600; color: var(--ink); line-height: 1.1; }
  .doctor-title { font-size: 17px; color: var(--brand-blue); margin-bottom: 10px; letter-spacing: .02em; }
  .contact-list { list-style: none; font-size: 14.5px; color: var(--text); line-height: 1.5; }
  .contact-list li { display: flex; gap: 10px; align-items: flex-start; }
  .contact-list svg { width: 13px; height: 13px; margin-top: 4px; flex: none; fill: var(--brand-blue); }
</style>
</head>
<body>

<section class="card card-front" aria-label="Card front">
  <div class="brand">
    <div class="mark-dot"></div>
    <p class="clinic-name">
      <span class="line-md">Amber Hollow</span>
      <span class="line-lg">Eye Care</span>
      <span class="line-sm">Optometry</span>
    </p>
  </div>
  <div class="web-band">amberholloweyecare.net</div>
</section>

<section class="card card-back" aria-label="Card back">
  <svg class="waves" viewBox="0 0 620 354" preserveAspectRatio="none" aria-hidden="true">
    <path d="M250 354 C380 300 520 250 620 110 L620 354 Z" fill="var(--pale-blue)" opacity=".6"/>
    <path d="M230 354 C380 310 540 260 620 150 L620 354 Z" fill="var(--sky-blue)"/>
    <path d="M0 354 L0 300 C160 275 330 300 470 260 C540 240 590 210 620 180 L620 354 Z" fill="var(--brand-blue)"/>
  </svg>
  <div class="brand">
    <div class="mark-dot"></div>
    <p class="clinic-name">
      <span class="line-md">Amber Hollow</span>
      <span class="line-lg">Eye Care</span>
      <span class="line-sm">Optometry</span>
    </p>
  </div>
  <div class="divider"></div>
  <div class="contact">
    <h1 class="doctor-name">Dr Selma Okonkwo</h1>
    <p class="doctor-title">OPTOMETRIST</p>
    <ul class="contact-list">
      <li><svg viewBox="0 0 24 24"><path d="M6.6 10.8a15 15 0 0 0 6.6 6.6l2.2-2.2a1 1 0 0 1 1-.25 11.4 11.4 0 0 0 3.6.6 1 1 0 0 1 1 1V20a1 1 0 0 1-1 1A17 17 0 0 1 3 4a1 1 0 0 1 1-1h3.5a1 1 0 0 1 1 1 11.4 11.4 0 0 0 .6 3.6 1 1 0 0 1-.25 1z"/></svg>604-555-0193</li>
      <li><svg viewBox="0 0 24 24"><path d="M2 5h20v14H2z M4 7v.5l8 5.5 8-5.5V7z" fill-rule="evenodd"/></svg>info@amberholloweyecare.net</li>
      <li><svg viewBox="0 0 24 24"><path d="M12 2a7 7 0 0 0-7 7c0 5 7 13 7 13s7-8 7-13a7 7 0 0 0-7-7zm0 9.5A2.5 2.5 0 1 1 12 6.5a2.5 2.5 0 0 1 0 5z"/></svg><span>312-617 E Larkspur Ave<br>Vancouver BC V7R 3P8</span></li>
    </ul>
  </div>
</section>

</body>
</html>
```